Kestin Power Battery advertisment for Facebook ads

Objective:
Design a compelling Facebook advertisement to promote the new Federal Government Home Battery Subsidy, encouraging existing solar customers to act now and install a battery system under the new subsidy program.

Key Message:

25kWh Battery System Installed from $9,800
Act now and secure your affordable energy future today!
Design Requirements:

Bold headline showcasing the 25kWh for $9,800 offer.
Clear reference to the Federal Government Battery Subsidy as the reason for the low pricing.
Include messaging around:
Claim your subsidy before it winds down—like the solar rebate, it reduces each year
The subsidy can only be claimed once per household—go large now to future-proof your energy needs
Add a strong Call to Action like: “Beat the Rush—Secure Your Battery Today!”

Target Market(s)

Home owners who want to add batteries to existing solar systems

Industry/Entity Type

Renewable energy

Colors
0054AA
0677BA
7BADD7
CADEEF
E8F1F8
EB3D1F
EC4F4E
F09395
F8D3D4
FCEDEE

Requirements
Must have
• Visual Style: Modern, clean, and high-trust Use imagery of solar homes, battery units, or families enjoying power security at night Include visual cues of savings, energy independence, or clean energy Mobile-optimized, designed for Facebook feed
Nice to have
• Tone: Confident, future-focused, and urgent—while remaining trustworthy and informative. I would like a picture of battery ideally VOM battery on a home or such
Should not have
• must be professional and be a call to action

```html
<!DOCTYPE html>
<html lang="en">
<head>
<meta charset="utf-8">
<title>Kestin Power – Home Battery Offer</title>
<link rel="stylesheet" href="https://fonts.googleapis.com/css2?family=Cinzel:wght@700;800&family=Roboto:wght@400;700&display=swap">
<style>
  :root {
    --cream: #faf7f0;
    --navy: #2b3344;
    --red: #b71f2d;
    --band-red: #c01f2e;
    --ink: #262626;
    --white: #ffffff;
  }
  * { margin: 0; padding: 0; box-sizing: border-box; }
  html, body { width: 1200px; height: 1200px; overflow: hidden; background: var(--cream); }
  .ad {
    position: relative;
    width: 1200px;
    height: 1200px;
    background: var(--cream);
    font-family: "Roboto", Arial, sans-serif;
    color: var(--ink);
    overflow: hidden;
  }
  .brand {
    position: absolute;
    left: 89px;
    top: 78px;
  }
  .brand-name {
    font-family: "Roboto", Arial, sans-serif;
    font-weight: 700;
    font-size: 54px;
    line-height: 1;
    color: var(--navy);
  }
  .brand-tagline {
    margin-top: 36px;
    font-size: 17px;
    letter-spacing: 0.4px;
    color: var(--navy);
  }
  .battery-photo {
    position: absolute;
    right: 0; top: 0;
    width: 280px; height: 435px;
    background: linear-gradient(90deg, rgba(250,247,240,0) 0%, #ecebe8 25%, #f4f4f2 70%, #d9d7d2 100%);
    -webkit-mask-image: linear-gradient(180deg, #000 70%, transparent 100%);
    mask-image: linear-gradient(180deg, #000 70%, transparent 100%);
  }
  .headline {
    position: absolute;
    left: 89px;
    top: 258px;
    font-family: "Cinzel", Georgia, serif;
    font-weight: 800;
    font-size: 90px;
    line-height: 104px;
    letter-spacing: -1px;
    color: var(--navy);
    text-transform: uppercase;
  }
  .headline .accent { color: var(--red); }
  .lead {
    position: absolute;
    left: 89px;
    top: 577px;
    width: 860px;
    font-size: 51px;
    line-height: 75px;
    color: var(--ink);
  }
  .subsidy {
    position: absolute;
    left: 89px;
    top: 748px;
    font-weight: 700;
    font-size: 43px;
    line-height: 59px;
    color: var(--ink);
  }
  .benefits {
    position: absolute;
    left: 89px;
    top: 886px;
    width: 800px;
    list-style: none;
  }
  .benefits li {
    position: relative;
    padding-left: 57px;
    font-size: 28px;
    line-height: 42px;
    margin-bottom: 1px;
  }
  .benefits li::before {
    content: "";
    position: absolute;
    left: 2px; top: 11px;
    width: 20px; height: 20px;
    border: 3px solid var(--red);
  }
  .home-photo {
    position: absolute;
    left: 944px;
    width: 256px;
  }
  .home-photo.sky {
    top: 572px; height: 256px;
    border-radius: 150px 0 0 0;
    background: linear-gradient(180deg, #5c8fd0 0%, #9fc0e6 55%, #3a5a3e 100%);
  }
  .home-photo.lawn {
    top: 839px; height: 255px;
    background: linear-gradient(180deg, #6b6f7a 0%, #8a7a6a 40%, #5f9a3a 75%, #c9c6c0 100%);
  }
  .cta-band {
    position: absolute;
    left: 0; bottom: 0;
    width: 1200px; height: 95px;
    background: var(--band-red);
    display: flex;
    align-items: center;
  }
  .cta-text {
    margin-left: 184px;
    font-weight: 700;
    font-size: 40px;
    color: var(--white);
    letter-spacing: 0.3px;
  }
  .cta-code {
    position: absolute;
    right: 22px; bottom: 18px;
    font-weight: 700;
    font-size: 18px;
    color: var(--white);
  }
</style>
</head>
<body>
<main class="ad">
  <header class="brand">
    <p class="brand-name">Kestin Power</p>
    <p class="brand-tagline">ENGINEERING AND ECONOMIC SOLUTIONS</p>
  </header>

  <div class="battery-photo" role="img" aria-label="Wall-mounted home battery inverter unit"></div>

  <h1 class="headline">
    <span class="accent">25kWh</span> Battery<br>
    System Installed<br>
    From <span class="accent">$9,800</span>
  </h1>

  <p class="lead">Act now and secure your affordable<br>energy future today!</p>

  <h2 class="subsidy">Thanks to the Federal Government's<br>new Home Battery Subsidy</h2>

  <ul class="benefits">
    <li>Claim your subsidy before it winds down—like the solar<br>rebate,it reduces each year</li>
    <li>The subsidy can only be claimed once per household<br>go large now to future-proof your energy needs</li>
  </ul>

  <div class="home-photo sky" role="img" aria-label="Solar panels on a house roof under blue sky"></div>
  <div class="home-photo lawn" role="img" aria-label="Brick home with rooftop solar and front lawn"></div>

  <footer class="cta-band">
    <p class="cta-text">BEAT THE RUSH—SECURE YOUR BATTERY TODAY!</p>
    <span class="cta-code">C9</span>
  </footer>
</main>
</body>
</html>
```